Restaurant Needs a Flyer Design for a Cocktail Competition

We are a Chinese restaurant specializing in hot pot cuisine. More information about our specialty and product line can be found on our website: www.brinskaleto.com.
We are expanding our bar menu and plan to hold a competition between local bartenders to craft new signature sake cocktails for our restaurant. We need someone to design a flyer that can be distributed to local bars and restaurants in order to catch their interest.
For the name of the competition, we were considering something along the lines of "Season of Sake - Brinska Leto's Cocktail Competition". However, more consideration will be given to designs that come up with an original, creative headline. The headline must reference that it is a "sake cocktail" competition to avoid any confusion.
The overall look of the flyer should be fun and eye-catching.
The information that we need included on the front of the flyer (not in this wording or order) is as follows:
1. Name of our restaurant, website, and location
2. The name of the competition
3. Submissions must be submitted to this email address: brinskaleto1@mailvane.com
4. The deadline for submissions is July 31st, 2015
5. Images to accompany the text as well as our logo
6. Eight finalists will be chosen by the restaurant's staff and the top three will be chosen by customer vote.
7. The top three will be awarded prizes:
a. Grand Prize Winner: The choice of either a
"Winner's Dinner" for them and their entire staff
OR a cash prize of $300
b. 2nd Prize Winner: $100 cash prize AND $100
Brinska Leto gift card
c. 3rd Prize Winner: $100 Brinska Leto gift card
8. ALL three winners will receive a credit under their winning drink on our menu - their bar/restaurant will be credited on the menu as well
9. The eight finalists will be chosen by August 10th, 2015 and the three winners will be chosen by August 31st, 2015.
On the back of the flyer we will include a list of our submission guidelines and contest rules. Those guidelines and rules are included as attachments at the bottom along with our logo.

```html
<!DOCTYPE html>
<html lang="en">
<head>
<meta charset="utf-8">
<title>Season of Sake - Brinska Leto's Cocktail Competition</title>
<link rel="stylesheet" href="https://fonts.googleapis.com/css2?family=Bebas+Neue&family=Montserrat:wght@700&display=swap">
<style>
  :root {
    --bg-deep: #3e2412;
    --bg-mid: #7a4520;
    --bg-glow: #c0733a;
    --brand-white: #ffffff;
    --cream-top: #f7ece0;
    --cream-bottom: #f0d6bf;
    --pink-top: #f6dfe6;
    --pink-bottom: #e567ad;
    --edge: #fff6f1;
    --glow-orange: rgba(255, 170, 90, 0.9);
    --glow-pink: rgba(255, 150, 170, 0.85);
  }
  html, body {
    margin: 0;
    padding: 0;
    width: 1200px;
    height: 1000px;
    overflow: hidden;
  }
  .flyer {
    position: relative;
    width: 1200px;
    height: 1000px;
    overflow: hidden;
    background: var(--bg-deep);
  }
  .sparkle-backdrop {
    position: absolute;
    inset: 0;
    background:
      radial-gradient(ellipse 55% 40% at 45% 62%, rgba(235, 150, 90, 0.55), transparent 70%),
      radial-gradient(ellipse 40% 30% at 20% 30%, rgba(200, 120, 60, 0.35), transparent 70%),
      linear-gradient(180deg, #5a3419 0%, var(--bg-mid) 45%, var(--bg-glow) 70%, #6b3a1a 100%);
  }
  .brand-name {
    position: absolute;
    left: 995px;
    top: 70px;
    margin: 0;
    font-family: "Montserrat", sans-serif;
    font-weight: 700;
    font-size: 50px;
    letter-spacing: -1px;
    color: var(--brand-white);
    white-space: nowrap;
    line-height: 1;
  }
  .headline {
    margin: 0;
    font-family: "Bebas Neue", sans-serif;
    font-weight: 400;
  }
  .headline-line {
    position: absolute;
    display: block;
    white-space: nowrap;
    line-height: 1;
    letter-spacing: 4px;
  }
  .headline-line::before {
    content: attr(data-text);
    position: absolute;
    left: 5px;
    top: 5px;
    color: transparent;
    -webkit-text-stroke: 3px var(--edge);
    z-index: 0;
  }
  .headline-line .fill {
    position: relative;
    z-index: 1;
    color: transparent;
    -webkit-background-clip: text;
    background-clip: text;
    -webkit-text-stroke: 2px var(--edge);
  }
  .headline-season {
    left: 52px;
    top: 117px;
    font-size: 520px;
    filter: drop-shadow(0 0 18px var(--glow-orange));
  }
  .headline-season .fill {
    background-image: linear-gradient(180deg, var(--cream-top), var(--cream-bottom));
  }
  .headline-event {
    left: 62px;
    top: 566px;
    font-size: 370px;
    filter: drop-shadow(0 0 16px var(--glow-pink));
  }
  .headline-event .fill {
    background-image: linear-gradient(180deg, var(--pink-top) 0%, #f1bcd2 55%, var(--pink-bottom) 100%);
  }
</style>
</head>
<body>
  <main class="flyer">
    <div class="sparkle-backdrop" role="img" aria-label="Warm amber background filled with glowing golden sparkles and bokeh lights"></div>
    <p class="brand-name">BRINSKA LETO</p>
    <h1 class="headline">
      <span class="headline-line headline-season" data-text="SUMMER"><span class="fill">SUMMER</span></span>
      <span class="headline-line headline-event" data-text="COCKTAIL COMPETITION"><span class="fill">COCKTAIL COMPETITION</span></span>
    </h1>
  </main>
</body>
</html>
```